依頼詳細
12月下旬~1月上旬オープンに向けてのチラシ作成をお願いいたします。オープン以降も同じチラシを定期的にポスティングいたしますので汎用できるようにお願いいたします。
納品はaiデータでお願いいたします。
記載項目
社名や電話番号は後で投稿させていただきます。
サイズ
A4
ページ数
片面
希望イメージ
シンプル 複雑
単色 カラフル
暗い 明るい
日常 高級
遊び心 厳粛
未来的 伝統的
女性的 男性的
希望する色
水色系
納品ファイル
• イラストレーター形式 (.ai)
補足説明
脱毛サロンのロゴを貼り付けさせていただきます。
脱毛器の画像や使用イメージ画像を追加させていただきます。
よろしくお願いいたします。
作成していただいているところに追記すみません。
オープン期間限定キャンペーン→その後、通常価格に戻します。
メニュー内容につきましては
30分→通常3500円
60分→通常4500円
月額会員→通常5500円(初月のみ)
全メニュー1000円off!!
ずーっと会員登録費・事務手数料【無料】
■ 選んだ理由

わかりやすさ。色合い

■ 提案者全員のお礼・コメント

今回たくさんのご応募いただきありがとうございます。
また、どの提案も素敵なもので決めるのに苦慮しました。またよろしくお願いいたします。

```html
<!DOCTYPE html>
<html lang="ja">
<head>
<meta charset="utf-8">
<title>ルミナ セルフ脱毛サロン オープンチラシ</title>
<link href="https://fonts.googleapis.com/css2?family=M+PLUS+Rounded+1c:wght@400;700;800&family=Noto+Sans+JP:wght@400;700;900&family=Quicksand:wght@400;500&family=Dancing+Script:wght@700&display=swap" rel="stylesheet">
<style>
:root{
  --sky:#dff1f8;
  --sky-mid:#a9dcef;
  --blue:#4fb3dc;
  --blue-deep:#2a8fc0;
  --teal-logo:#6cb9c9;
  --white:#ffffff;
  --red:#e3312d;
  --orange:#f3a33a;
  --orange-deep:#e77f1b;
  --ink:#333a40;
  --grey:#8a9499;
  --photo-skin:#e9d3c6;
  --photo-cool:#cfe3ec;
}
*{margin:0;padding:0;box-sizing:border-box}
html,body{width:846px;height:1200px;overflow:hidden;background:var(--white)}
body{font-family:"Noto Sans JP",sans-serif;color:var(--ink)}
.flyer{position:relative;width:846px;height:1200px;overflow:hidden;
  background:linear-gradient(180deg,var(--sky) 0%,#eef8fc 60%,var(--sky) 100%)}
.abs{position:absolute}
.bg-diamonds{position:absolute;inset:0}

/* opening banner */
.open-banner{position:absolute;left:-75px;top:83px;width:360px;height:60px;background:var(--red);
  transform:rotate(-45deg);color:var(--white);display:flex;align-items:center;justify-content:center;
  font-family:"M PLUS Rounded 1c",sans-serif;font-weight:800;font-size:25px;letter-spacing:1px;white-space:nowrap;box-shadow:0 3px 0 rgba(0,0,0,.1)}
.open-banner small{font-size:16px;margin:0 3px}

/* category badge */
.category{position:absolute;left:465px;top:4px;width:150px;height:70px;color:var(--white);
  font-family:"M PLUS Rounded 1c",sans-serif;font-weight:700;font-size:19px;text-align:center;line-height:1.25;
  display:flex;align-items:center;justify-content:center;
  background:var(--blue);clip-path:polygon(10% 0,90% 0,100% 50%,90% 100%,10% 100%,0 50%)}

/* main logo diamond */
.logo-diamond{position:absolute;left:365px;top:90px;width:350px;height:350px;background:var(--white);
  clip-path:polygon(50% 0,100% 50%,50% 100%,0 50%)}
.logo-block{position:absolute;left:365px;top:90px;width:350px;height:350px;text-align:center;
  display:flex;flex-direction:column;align-items:center;justify-content:center}
.brand-mark{width:34px;height:34px;border-radius:50%;background:var(--teal-logo);margin-bottom:8px}
.brand-name{font-family:"Quicksand",sans-serif;font-weight:400;font-size:78px;color:var(--teal-logo);line-height:1}
.brand-kana{font-family:"Quicksand",sans-serif;font-size:22px;color:var(--teal-logo);letter-spacing:8px;margin-top:4px}
.site-url{font-size:13px;color:var(--grey);margin-top:22px}

/* photos */
.photo{position:absolute}
.diamond{clip-path:polygon(50% 0,100% 50%,50% 100%,0 50%)}

/* speech bubbles */
.bubble{position:absolute;border-radius:50%;background:var(--white);border:2px solid var(--blue);
  display:flex;align-items:center;justify-content:center;text-align:center;
  font-family:"M PLUS Rounded 1c",sans-serif;font-weight:700;font-size:14px;line-height:1.3;color:var(--blue-deep)}
.bubble .text{display:block;white-space:nowrap}
.bubble.orange{border-color:var(--orange);color:var(--orange-deep)}
.bubble .hl{color:var(--orange-deep)}

.catch{position:absolute;font-family:"M PLUS Rounded 1c",sans-serif;font-weight:800;line-height:1.35}
.catch.blue{color:var(--blue-deep)}
.catch.orange{color:var(--orange-deep)}

/* feature icons */
.features{position:absolute;left:30px;top:470px;display:flex;gap:14px}
.feature{width:72px;text-align:center;font-size:11px;font-weight:700;color:var(--orange-deep)}
.feature .tile{width:60px;height:60px;margin:0 auto 4px;background:var(--orange);border-radius:6px;
  display:flex;align-items:center;justify-content:center}

.machine-label{position:absolute;left:30px;top:568px;width:250px;background:var(--blue);color:var(--white);
  font-family:"M PLUS Rounded 1c",sans-serif;font-weight:800;font-size:24px;line-height:1.3;padding:8px 14px}

/* menu */
.menu-title{position:absolute;left:470px;top:672px;font-family:"Quicksand",sans-serif;font-weight:500;
  font-size:30px;letter-spacing:4px;color:var(--blue-deep)}
.menu{position:absolute;left:420px;top:720px;width:190px}
.menu-row{display:flex;align-items:center;height:58px}
.menu-tag{width:40px;height:40px;flex:none;background:var(--blue);color:var(--white);font-size:11px;font-weight:700;
  line-height:1.05;display:flex;align-items:center;justify-content:center;text-align:center;
  clip-path:polygon(50% 0,100% 50%,50% 100%,0 50%)}
.menu-price{margin-left:6px;font-weight:900;font-size:32px;color:var(--blue-deep);line-height:1;white-space:nowrap}
.menu-price small{font-size:12px;font-weight:700;color:var(--ink);margin-right:2px}
.menu-price .yen{font-size:19px}
.menu-price .note{display:block;font-size:11px;font-weight:700;color:var(--ink);text-align:right}

.campaign{position:absolute;left:614px;top:735px;width:218px;height:205px;background:var(--white);
  border:3px solid var(--red);text-align:center;padding-top:8px;color:var(--red)}
.campaign .lead{font-family:"M PLUS Rounded 1c",sans-serif;font-weight:800;font-size:19px;line-height:1.2}
.campaign .all{display:inline-block;background:var(--red);color:var(--white);font-weight:700;font-size:13px;padding:2px 10px;margin-top:6px}
.campaign .was{font-size:11px;color:var(--ink);margin-left:6px}
.campaign .off{font-weight:900;font-size:32px;line-height:1.15;margin-top:2px}
.campaign .off small{font-size:18px}
.campaign .fine{font-size:9px;color:var(--ink);line-height:1.4;margin:4px 10px 0;text-align:left}

.always{position:absolute;left:420px;top:905px;width:190px;text-align:center}
.always .pill{display:inline-block;background:var(--blue);color:var(--white);font-weight:700;font-size:13px;
  padding:2px 14px;border-radius:12px}
.always .label{font-weight:700;font-size:15px;color:var(--blue-deep);margin-top:6px;white-space:nowrap}
.always .free{font-family:"M PLUS Rounded 1c",sans-serif;font-weight:800;font-size:34px;color:var(--blue-deep);line-height:1.1}

.model-name{position:absolute;left:48px;top:1068px;font-family:"Dancing Script",cursive;font-size:30px;color:var(--orange-deep)}

/* map */
.map{position:absolute;left:636px;top:955px;width:200px;height:150px;background:var(--white);border:1px solid #c9d4d8}

/* footer */
.footer{position:absolute;left:0;top:1112px;width:846px;height:88px;background:var(--white);border-top:3px solid var(--blue);
  display:flex;align-items:center;padding:0 28px;gap:26px}
.footer-brand{text-align:center;color:var(--teal-logo);font-family:"Quicksand",sans-serif}
.footer-brand .name{font-size:34px;line-height:1}
.footer-brand .kana{font-size:11px;letter-spacing:4px}
.contact{flex:1}
.contact .ask{font-size:11px;color:var(--white);background:var(--blue);display:inline-block;padding:1px 10px;border-radius:8px}
.contact .lines{display:flex;gap:22px;align-items:center;margin-top:4px}
.contact .tel{font-weight:900;font-size:26px;color:var(--blue-deep)}
.contact .mail{font-weight:700;font-size:16px;color:var(--blue-deep);display:flex;align-items:center;gap:6px}
.contact .addr{font-size:10px;color:var(--grey);margin-top:3px}
</style>
</head>
<body>
<main class="flyer">

  <svg class="bg-diamonds" width="846" height="1200" aria-hidden="true">
    <polygon points="200,300 330,430 200,560 70,430" fill="#cde9f5"/>
    <polygon points="700,560 820,680 700,800 580,680" fill="#cde9f5"/>
    <polygon points="120,700 200,780 120,860 40,780" fill="#e6f5fb"/>
    <polygon points="350,40 390,80 350,120 310,80" fill="#bfe3f2"/>
    <polygon points="800,900 830,930 800,960 770,930" fill="#bfe3f2"/>
  </svg>

  <div class="open-banner">0月10日<small>(月)</small>OPEN!</div>

  <div class="category">セルフ脱毛<br>サロン</div>

  <div class="photo diamond" role="img" aria-label="照射機で施術を受ける人の写真"
       style="left:-40px;top:170px;width:290px;height:300px;background:linear-gradient(135deg,var(--photo-cool),var(--photo-skin))"></div>
  <div class="photo diamond" role="img" aria-label="腕のムダ毛をケアする女性の写真"
       style="left:670px;top:20px;width:210px;height:230px;background:linear-gradient(135deg,#f3e2d8,var(--photo-skin))"></div>

  <div class="logo-diamond"></div>
  <div class="logo-block">
    <div class="brand-mark"></div>
    <div class="brand-name">lumina</div>
    <div class="brand-kana">-ルミナ-</div>
    <div class="site-url">http://dammy.oooooo</div>
  </div>

  <div class="bubble" style="left:168px;top:60px;width:110px;height:110px">
    <span class="text">お手軽な<br><span class="hl">価格</span>で<br>通いやすい!</span>
  </div>
  <div class="bubble" style="left:288px;top:66px;width:100px;height:100px;font-size:13px">
    <span class="text">セルフだから<br><span class="hl">恥ずかしく</span><br>ない!</span>
  </div>
  <div class="catch blue" style="right:18px;top:210px;font-size:19px;text-align:right">誰にも<br>見られずに<br>簡単に</div>
  <div class="bubble orange" style="left:728px;top:320px;width:96px;height:96px;font-size:14px">
    <span class="text">お子様の<br>悩みも<br>解決!</span>
  </div>
  <div class="catch orange" style="left:532px;top:402px;font-size:21px">お子様でも脱毛できる<br>安心安全な機材です!</div>

  <div class="photo" role="img" aria-label="並んで笑顔を見せる家族と子どもたちのイラスト"
       style="left:430px;top:475px;width:380px;height:190px;border-radius:6px;background:linear-gradient(180deg,#fbe6d6,#c7e4f1)"></div>

  <div class="features">
    <div class="feature">
      <div class="tile"><svg width="34" height="34" viewBox="0 0 34 34"><path d="M8 4h10l8 8v18H8z" fill="#fff"/><path d="M12 18l4 4 7-8" stroke="#f3a33a" stroke-width="3" fill="none"/></svg></div>
      操作簡単
    </div>
    <div class="feature">
      <div class="tile"><svg width="34" height="34" viewBox="0 0 34 34"><path d="M17 30C6 22 3 16 3 11a7 7 0 0 1 14-2 7 7 0 0 1 14 2c0 5-3 11-14 19z" fill="#fff"/></svg></div>
      安全
    </div>
    <div class="feature">
      <div class="tile"><svg width="34" height="34" viewBox="0 0 34 34"><polygon points="17,3 21,13 32,13 23,20 26,31 17,24 8,31 11,20 2,13 13,13" fill="#fff"/></svg></div>
      親切対応
    </div>
  </div>

  <div class="machine-label">高級脱毛マシンを<br>使い放題</div>

  <div class="photo" role="img" aria-label="業務用脱毛マシン本体の写真"
       style="left:60px;top:660px;width:300px;height:400px;border-radius:8px;background:linear-gradient(135deg,#ffffff,#d8e3e8)"></div>

  <div class="model-name">Glow Pulse</div>

  <div class="menu-title">MENU</div>
  <div class="menu">
    <div class="menu-row"><div class="menu-tag">30<br>分</div><div class="menu-price"><small>通常</small>3,500<span class="yen">円</span></div></div>
    <div class="menu-row"><div class="menu-tag">60<br>分</div><div class="menu-price"><small>通常</small>4,500<span class="yen">円</span></div></div>
    <div class="menu-row"><div class="menu-tag">月額<br>会員</div><div class="menu-price"><small>通常</small>5,500<span class="yen">円</span><span class="note">(初月のみ)</span></div></div>
  </div>

  <div class="campaign">
    <div class="lead">期間限定<br>オープンキャンペーン</div>
    <div><span class="all">全メニュー</span><span class="was">通常価格より</span></div>
    <div class="off">1,000<small>円</small>OFF!!</div>
    <div class="fine">※キャンペーン期間終了後は<br>通常価格に戻ります。</div>
  </div>

  <div class="always">
    <span class="pill">ずーっと</span>
    <div class="label">会員登録費・事務手数料</div>
    <div class="free">無料!</div>
  </div>

  <div class="map" role="img" aria-label="店舗までのアクセス地図"></div>

  <footer class="footer">
    <div class="footer-brand">
      <div class="name">lumina</div>
      <div class="kana">ルミナ</div>
    </div>
    <div class="contact">
      <span class="ask">お気軽にお問い合わせください</span>
      <div class="lines">
        <span class="tel">TEL.00-0000-0000</span>
        <span class="mail"><svg width="18" height="14" viewBox="0 0 18 14"><rect x="1" y="1" width="16" height="12" fill="none" stroke="#2a8fc0" stroke-width="1.6"/><path d="M1 1l8 7 8-7" fill="none" stroke="#2a8fc0" stroke-width="1.6"/></svg>info@000000</span>
      </div>
      <div class="addr">営業時間 00:00〜00:00 ／ 〒000-0000 ○○県○○市○○町0-0-0</div>
    </div>
  </footer>

</main>
</body>
</html>
```